Bref créative
Brightwave IT Business cards
Professional
Kenneth Darrow
Chief Information Officer
248 Maple Hollow Rd
KDarrow@BrightwaveIT.example
www.brightwaveit.example
IT managed services
Managed backups
Web Hosting
Email Hosting
Spam Filtering
Networking
Structured Cabling
Project Planning
Colocation Services

```html
<!DOCTYPE html>
<html lang="en">
<head>
<meta charset="utf-8">
<title>Brightwave IT Business Cards</title>
<link href="https://fonts.googleapis.com/css2?family=Arimo:wght@400;700&display=swap" rel="stylesheet">
<style>
  :root {
    --page: #e9edf1;
    --navy: #0f4c8c;
    --blue: #1f6fc0;
    --sky: #5fa7e3;
    --ice: #e6f1fb;
    --ink: #123f73;
    --muted: #3d5f86;
    --white: #ffffff;
  }
  * { margin: 0; padding: 0; box-sizing: border-box; }
  html, body { width: 1200px; height: 874px; overflow: hidden; }
  body {
    background: var(--page);
    font-family: "Arimo", Arial, sans-serif;
    position: relative;
  }
  .card {
    position: absolute;
    width: 660px;
    height: 404px;
    overflow: hidden;
    background: var(--white);
    box-shadow: 0 6px 18px rgba(20, 40, 70, 0.18);
  }
  .card-front { left: 30px; top: 20px; }
  .card-back { left: 510px; top: 450px; }
  .card-art { position: absolute; inset: 0; }
  .brand {
    position: absolute;
    left: 150px;
    top: 40px;
    display: flex;
    align-items: center;
    gap: 14px;
  }
  .brand-dot {
    width: 44px; height: 44px; border-radius: 50%;
    background: var(--blue);
  }
  .brand-name {
    font-size: 46px;
    font-weight: 700;
    color: var(--navy);
    letter-spacing: 0.5px;
  }
  .side-name {
    position: absolute;
    left: 10px;
    top: 40px;
    writing-mode: vertical-rl;
    font-size: 26px;
    font-weight: 700;
    color: rgba(255, 255, 255, 0.45);
    letter-spacing: 1px;
  }
  .person { position: absolute; left: 112px; top: 160px; }
  .person-name { font-size: 23px; font-weight: 700; color: var(--blue); }
  .person-title { font-size: 13px; color: var(--muted); margin-top: 3px; }
  .contact {
    position: absolute;
    left: 395px;
    top: 160px;
    list-style: none;
  }
  .contact li {
    display: flex;
    align-items: center;
    gap: 12px;
    height: 21px;
    font-size: 15px;
    color: var(--ink);
  }
  .contact svg { width: 15px; height: 15px; fill: var(--muted); flex: none; }
  .services-label {
    position: absolute;
    left: 260px;
    top: 242px;
    font-size: 16px;
    font-weight: 700;
    color: var(--white);
  }
  .services {
    position: absolute;
    left: 40px;
    top: 276px;
    display: grid;
    grid-template-columns: 162px 106px 118px 180px;
    row-gap: 6px;
    list-style: none;
  }
  .services li {
    display: flex;
    align-items: center;
    gap: 7px;
    font-size: 14px;
    color: var(--white);
    white-space: nowrap;
  }
  .services li::before {
    content: "";
    width: 9px; height: 9px; border-radius: 50%;
    background: radial-gradient(circle at 35% 35%, #d8ecff, var(--sky));
    flex: none;
  }
  .services .gap { visibility: hidden; }
</style>
</head>
<body>

<section class="card card-front" aria-label="Business card front">
  <svg class="card-art" viewBox="0 0 660 404" preserveAspectRatio="none" aria-hidden="true">
    <defs>
      <linearGradient id="frontSky" x1="0" y1="0" x2="1" y2="1">
        <stop offset="0" stop-color="#ffffff"/>
        <stop offset="0.6" stop-color="#eef5fc"/>
        <stop offset="1" stop-color="#cfe3f6"/>
      </linearGradient>
      <linearGradient id="sideBand" x1="0" y1="0" x2="1" y2="0">
        <stop offset="0" stop-color="#0c3f78"/>
        <stop offset="1" stop-color="#3f8fd6"/>
      </linearGradient>
      <linearGradient id="panel" x1="0" y1="0" x2="0" y2="1">
        <stop offset="0" stop-color="#2a7fd0"/>
        <stop offset="1" stop-color="#0f4c8c"/>
      </linearGradient>
    </defs>
    <rect width="660" height="404" fill="url(#frontSky)"/>
    <path d="M0 0 H70 C52 120 60 230 120 404 H0 Z" fill="url(#sideBand)"/>
    <path d="M70 0 C58 120 66 230 126 404" fill="none" stroke="#9cc8ef" stroke-width="3"/>
    <path d="M34 238 H325 L340 255 H660 V262 H34 Z" fill="#2f86d6"/>
    <path d="M34 262 H660 V350 C520 372 380 360 230 380 C150 390 90 382 34 372 Z" fill="url(#panel)"/>
    <path d="M34 372 C90 382 150 390 230 380 C380 360 520 372 660 350" fill="none" stroke="#8fc1ee" stroke-width="2"/>
  </svg>

  <span class="side-name" aria-hidden="true">Brightwave IT</span>

  <div class="brand">
    <span class="brand-dot"></span>
    <span class="brand-name">Brightwave IT</span>
  </div>

  <div class="person">
    <p class="person-name">Kenneth Darrow</p>
    <p class="person-title">Chief Information Officer</p>
  </div>

  <ul class="contact">
    <li><svg viewBox="0 0 16 16"><path d="M1 3h14v10H1z M3 5v6h10V5z"/></svg>248 Maple Hollow Rd</li>
    <li><svg viewBox="0 0 16 16"><path d="M3 1h3l1 4-2 1c1 2 3 4 5 5l1-2 4 1v3c0 1-1 2-2 2C7 15 1 9 1 3c0-1 1-2 2-2z"/></svg>512-555-0147</li>
    <li><svg viewBox="0 0 16 16"><path d="M1 3h14v10H1z M2 4l6 5 6-5v-0.5H2z" fill-rule="evenodd"/></svg>KDarrow@BrightwaveIT.example</li>
    <li><svg viewBox="0 0 16 16"><path d="M8 1l2 5h5l-4 3 2 6-5-4-5 4 2-6-4-3h5z"/></svg>www.brightwaveit.example</li>
  </ul>

  <p class="services-label">Services</p>
  <ul class="services">
    <li>IT managed services</li>
    <li>Web Hosting</li>
    <li>Spam Filtering</li>
    <li>Structured Cabling</li>
    <li>Managed backups</li>
    <li>Email Hosting</li>
    <li>Networking</li>
    <li>Project Planning</li>
    <li class="gap"></li>
    <li class="gap"></li>
    <li class="gap"></li>
    <li>Colocation Services</li>
  </ul>
</section>

<section class="card card-back" aria-label="Business card back">
  <svg class="card-art" viewBox="0 0 660 404" preserveAspectRatio="none" aria-hidden="true">
    <defs>
      <linearGradient id="backSky" x1="0" y1="0" x2="1" y2="1">
        <stop offset="0" stop-color="#ffffff"/>
        <stop offset="0.7" stop-color="#eef5fc"/>
        <stop offset="1" stop-color="#d6e8f8"/>
      </linearGradient>
      <linearGradient id="backBand" x1="0" y1="0" x2="1" y2="0">
        <stop offset="0" stop-color="#0c3f78"/>
        <stop offset="1" stop-color="#4a97db"/>
      </linearGradient>
    </defs>
    <rect width="660" height="404" fill="url(#backSky)"/>
    <path d="M0 0 H60 C46 120 56 250 110 404 H0 Z" fill="url(#backBand)"/>
    <path d="M60 0 C48 120 58 250 116 404" fill="none" stroke="#a6cdef" stroke-width="3"/>
    <path d="M0 330 C160 300 380 330 660 280 V404 H0 Z" fill="#e3eef9" opacity="0.7"/>
  </svg>
</section>

</body>
</html>
```